Grounded Inward: Renew Every Venture Through Five Pillars of Harvest

I'm looking for a design that is clean, like the book "Quiet Rivers" by Lionel Fraske. The book is about the principles of organic farming so I am looking for a color scheme that fits that image.
https://www.pagevendrix.com/Quiet-Rivers-Stillness-Hearing-Things-ebook/dp/K29Q844TXZ/ref=sr_1_3?crid=47MLP22QT55D1&keywords=lionel+fraske&qid=5729403382&s=books&sprefix=lionel+%2Cstripbooks%2C371&sr=1-3

I don't want a dark color scheme. I prefer a white or cream book with a bold font.

This book is a good example of what I am looking for:

https://www.pagevendrix.com/Lantern-Many-Lessons-Sketching-Days/dp/7741290358/ref=rtpb_2/512-7730418-2261947?pd_rd_w=qm8k2&pf_rd_p=31c9e276-518a-4f07-a6d2-e80b19c3a7d1&pf_rd_r=KP3T7NM2841B60WQLX5A&pd_rd_r=d417a6c0-2e95-4b6a-bc18-53f9e1a08c74&pd_rd_wg=3h5Xr&pd_rd_i=7741290358&psc=1

Target Market(s)

CEOs and business owners who want to increase the trust in their brands

Industry/Entity Type

Management and Leadership

Colors
00AB8E
00BBA5
67D7C9
C6EFE9
E9F9F6
59FF00
82FF00
B8FF75
E3FFCB
F4FFEA
FFF300
FFF600
FEFA6F
FFFEC7
FFFEE8
FFC000
F8CF3A
FAE287
FDF2CF
FEFAEE

Requirements
Must have
• Author's name is: Marcus Vellory
Nice to have
• I have indicated some books that I like. I would be good to have a simple image such as an apple core or the earth's core or some other image of "core" but not absolutely necessary.
Should not have
• I don't want it to have a dark cover or be too heavy

```html
<!DOCTYPE html>
<html lang="en">
<head>
<meta charset="utf-8">
<title>Grounded Inward — Marcus Vellory</title>
<link rel="stylesheet" href="https://fonts.googleapis.com/css2?family=Josefin+Sans:wght@400;600&display=swap">
<style>
  :root {
    --backdrop: #f2f2f2;
    --paper: #ffffff;
    --leaf-green: #a3d15a;
    --harvest-orange: #f8c46c;
    --core-cream: #fde3a6;
    --core-light: #fff3d6;
  }
  * { margin: 0; padding: 0; box-sizing: border-box; }
  html, body {
    width: 1129px;
    height: 1200px;
    overflow: hidden;
    background: var(--backdrop);
  }
  .book-cover {
    position: absolute;
    left: 255px;
    top: 137px;
    width: 618px;
    height: 923px;
    background: var(--paper);
    border: 3px solid;
    border-image: linear-gradient(to bottom, var(--harvest-orange), var(--leaf-green)) 1;
    font-family: "Josefin Sans", sans-serif;
    font-weight: 600;
    text-align: center;
    text-transform: uppercase;
  }
  .book-title { font-size: 62px; font-weight: 600; }
  .title-line {
    position: absolute;
    left: 0;
    width: 100%;
    height: 60px;
    line-height: 60px;
    white-space: nowrap;
    letter-spacing: 1px;
    color: var(--leaf-green);
  }
  .title-accent { color: var(--harvest-orange); }
  .line-1 { top: 60px; }
  .line-2 { top: 119px; }
  .line-3 { top: 178px; }
  .line-4 { top: 702px; }
  .line-5 { top: 769px; }
  .core-illustration {
    position: absolute;
    left: 119px;
    top: 240px;
    width: 374px;
    height: 440px;
    border-radius: 40% 40% 30% 30%;
    background: linear-gradient(to bottom, var(--leaf-green) 0%, var(--core-cream) 30%, var(--core-light) 60%, var(--core-cream) 82%, var(--leaf-green) 100%);
  }
  .author-rule {
    position: absolute;
    left: 194px;
    top: 828px;
    width: 241px;
    height: 1px;
    background: var(--leaf-green);
  }
  .author-name {
    position: absolute;
    left: 0;
    top: 843px;
    width: 100%;
    font-size: 31px;
    font-weight: 400;
    letter-spacing: 1px;
    white-space: nowrap;
    color: var(--leaf-green);
  }
</style>
</head>
<body>
  <main class="book-cover">
    <h1 class="book-title">
      <span class="title-line line-1">Renew</span>
      <span class="title-line line-2 title-accent">Every Venture</span>
      <span class="title-line line-3">Through Five</span>
      <span class="title-line line-4">Pillars of</span>
      <span class="title-line line-5">Harvest</span>
    </h1>
    <div class="core-illustration" role="img" aria-label="Illustration of a green apple core with stem and seeds"></div>
    <div class="author-rule"></div>
    <p class="author-name">Marcus Vellory</p>
  </main>
</body>
</html>
```